VEK.PRO- Daniel Whitcombe Fitness- needs a clever business card using the logo, name, info, contact

I need a business card designed for my Online Personal Training company called VEK.PRO, abbreviation for Daniel Whitcombe Fitness. My company focuses on coaching in personal health and personal growth to unleash your greatest potential. I would like to see designs that use my color scheme of a redish-orange (C:0,M:84,Y:100,K:0), grey, white, black, and my company font is OSWALD. The final design should communicate some aspects of design, health, motivation, growth, in some way. The logo is very important to the company and can be displayed in any of the colors previously mentioned. Must include the company name, my website: www.vek.example , my email: dan@vek.example

Target Market(s)

Personal health, fitness, general public, those who lack knowledge, awareness, and confidence in personal health

Industry/Entity Type

Personal Trainer

Font styles to use
Other font styles liked:
• OSWALD. (Bold, Regular, Light)

Colors
f37122
ffffff
9d9d9d
000000

Requirements
Must have
• Must include the logo, company name, my website: www.vek.example , my email: dan@vek.example
Nice to have
• Variations of the colors scheme of a redish-orange (C:0,M:84,Y:100,K:0), grey, white, black. Logo, card, or text can be in any of these colors.
• Possible quote like "Take control of your personal health to unleash your greatest potential" or "Unleashing your greatness first begins with fitness of the body and mind"

```html
<!DOCTYPE html>
<html lang="en">
<head>
<meta charset="utf-8">
<title>VEK.PRO – Business Card</title>
<link href="https://fonts.googleapis.com/css2?family=Oswald:wght@300;400;500;700&display=swap" rel="stylesheet">
<style>
  :root {
    --bg: #4a4a4a;
    --card: #2a2627;
    --orange: #f04e23;
    --white: #ffffff;
    --grey: #d6d6d6;
  }
  html, body {
    margin: 0;
    padding: 0;
    width: 1200px;
    height: 1134px;
    overflow: hidden;
    background: var(--bg);
    font-family: "Oswald", sans-serif;
  }
  .canvas {
    position: relative;
    width: 1200px;
    height: 1134px;
  }
  .card {
    position: absolute;
    left: 261px;
    width: 675px;
    height: 380px;
    background: var(--card);
    border-radius: 14px;
    overflow: hidden;
    box-shadow: 0 6px 14px rgba(0,0,0,0.45);
  }
  .card--front { top: 161px; }
  .card--back { top: 590px; }

  .wordmark {
    position: absolute;
    color: var(--white);
    font-weight: 500;
    line-height: 1;
    letter-spacing: -0.5px;
  }
  .wordmark__name { display: block; }
  .wordmark__tag {
    display: block;
    font-weight: 300;
    letter-spacing: -0.3px;
  }
  .card--front .wordmark { left: 50px; top: 54px; }
  .card--front .wordmark__name { font-size: 46px; }
  .card--front .wordmark__tag { font-size: 13.5px; margin-top: 4px; }

  .person { position: absolute; left: 51px; top: 198px; }
  .person__name {
    color: var(--orange);
    font-size: 32px;
    font-weight: 500;
    line-height: 1;
    margin: 0;
  }
  .person__role {
    color: var(--grey);
    font-size: 21px;
    font-weight: 300;
    margin: 6px 0 0;
    line-height: 1;
  }

  .contact {
    position: absolute;
    left: 51px;
    top: 292px;
    margin: 0;
    padding: 0;
    list-style: none;
  }
  .contact__item {
    display: flex;
    align-items: center;
    gap: 9px;
    color: var(--grey);
    font-size: 15.5px;
    font-weight: 300;
    height: 23.5px;
  }
  .contact__icon { width: 16px; height: 16px; fill: var(--orange); }

  .badge {
    position: absolute;
    left: 288px;
    top: -4px;
    width: 388px;
    height: 388px;
  }
  .badge__text {
    position: absolute;
    inset: 0;
    display: flex;
    align-items: center;
    justify-content: center;
    color: var(--orange);
    font-size: 76px;
    font-weight: 700;
    letter-spacing: -1px;
  }

  .mark {
    position: absolute;
    left: 250px;
    top: 75px;
    width: 176px;
    height: 176px;
    border-radius: 50%;
    background: var(--orange);
  }
  .card--back .wordmark {
    left: 0;
    right: 0;
    top: 267px;
    text-align: center;
  }
  .card--back .wordmark__name { font-size: 36px; }
  .card--back .wordmark__tag { font-size: 10.5px; margin-top: 2px; }
</style>
</head>
<body>
<main class="canvas">

  <section class="card card--front">
    <div class="wordmark">
      <span class="wordmark__name">VEK.PRO</span>
      <span class="wordmark__tag">DANIEL WHITCOMBE.FITNESS</span>
    </div>

    <div class="person">
      <h1 class="person__name">ROWAN HALE</h1>
      <p class="person__role">President</p>
    </div>

    <ul class="contact">
      <li class="contact__item">
        <svg class="contact__icon" viewBox="0 0 24 24"><path d="M6.6 10.8a15.1 15.1 0 0 0 6.6 6.6l2.2-2.2c.3-.3.7-.4 1-.2 1.1.4 2.3.6 3.6.6.6 0 1 .4 1 1V20c0 .6-.4 1-1 1C10.6 21 3 13.4 3 4c0-.6.4-1 1-1h3.5c.6 0 1 .4 1 1 0 1.3.2 2.5.6 3.6.1.3 0 .7-.2 1L6.6 10.8z"/></svg>
        555 014 2298
      </li>
      <li class="contact__item">
        <svg class="contact__icon" viewBox="0 0 24 24"><path d="M2 5h20v2l-10 6L2 7V5zm0 4.3l10 6 10-6V19H2V9.3z"/></svg>
        dan@vek.example
      </li>
      <li class="contact__item">
        <svg class="contact__icon" viewBox="0 0 24 24"><path d="M12 2a10 10 0 1 0 0 20 10 10 0 0 0 0-20zm6.9 6h-2.9a15 15 0 0 0-1.4-3.9A8 8 0 0 1 18.9 8zM12 4c.8 1.2 1.5 2.5 1.9 4h-3.8c.4-1.5 1.1-2.8 1.9-4zM4.3 14a8 8 0 0 1 0-4h3.3a16 16 0 0 0 0 4H4.3zm.8 2h2.9c.3 1.4.8 2.7 1.4 3.9A8 8 0 0 1 5.1 16zM8 8H5.1a8 8 0 0 1 4.3-3.9C8.8 5.3 8.3 6.6 8 8zm4 12c-.8-1.2-1.5-2.5-1.9-4h3.8c-.4 1.5-1.1 2.8-1.9 4zm2.3-6H9.7a14 14 0 0 1 0-4h4.6a14 14 0 0 1 0 4zm.3 5.9c.6-1.2 1.1-2.5 1.4-3.9h2.9a8 8 0 0 1-4.3 3.9zm1.8-5.9a16 16 0 0 0 0-4h3.3a8 8 0 0 1 0 4h-3.3z"/></svg>
        www.vek.example
      </li>
    </ul>

    <div class="badge">
      <svg width="388" height="388" viewBox="0 0 388 388" aria-hidden="true">
        <circle cx="194" cy="194" r="192" fill="var(--white)"/>
        <circle cx="194" cy="194" r="178" fill="none" stroke="var(--orange)" stroke-width="3"/>
      </svg>
      <span class="badge__text">VEK.PRO</span>
    </div>
  </section>

  <section class="card card--back">
    <div class="mark" aria-hidden="true"></div>
    <div class="wordmark">
      <span class="wordmark__name">VEK.PRO</span>
      <span class="wordmark__tag">DANIEL WHITCOMBE.FITNESS</span>
    </div>
  </section>

</main>
</body>
</html>
```